Criação de Papelaria (6 itens) para Logística, Entrega & Armazenamento
" B.H.L. Cargo e uma empresa nova no mercado. Trabalha com transporte internacional de cargas, aéreo e marítimo. Estamos localizados na Av. Corvelha. Temos origem Chinesa. "

```html
<!DOCTYPE html>
<html lang="pt-BR">
<head>
<meta charset="UTF-8">
<title>B.H.L. Cargo — Cartão de Visita</title>
<link href="https://fonts.googleapis.com/css2?family=Open+Sans:wght@400;600;700;800&display=swap" rel="stylesheet">
<style>
  :root {
    --stage: #000000;
    --card: #ffffff;
    --card-soft: #f2f4f7;
    --brand-blue: #2a47b8;
    --navy: #123f72;
    --navy-deep: #0c2f58;
    --sky: #2fa9e2;
    --sky-light: #5cc3ee;
    --ink-blue: #1b4f8c;
    --ink-grey: #555b63;
    --watermark: #2c6fae;
  }
  * { margin: 0; padding: 0; box-sizing: border-box; }
  html, body {
    width: 1200px; height: 1200px; overflow: hidden;
    background: var(--stage);
    font-family: "Open Sans", Arial, sans-serif;
  }
  .stage { position: relative; width: 1200px; height: 1200px; }

  .card {
    position: absolute; left: 228px; width: 744px;
    background: linear-gradient(135deg, var(--card) 0%, var(--card-soft) 100%);
    overflow: hidden;
  }
  .card-front { top: 120px; height: 413px; display: flex; align-items: center; justify-content: center; }
  .brand-name {
    font-weight: 800; font-size: 92px; color: var(--brand-blue);
    letter-spacing: -1px; margin-top: 20px; white-space: nowrap;
  }

  .card-back { top: 636px; height: 401px; background: var(--card); }
  .back-art { position: absolute; inset: 0; }
  .holder { position: absolute; left: 43px; top: 36px; }
  .holder-name { font-size: 38px; font-weight: 600; color: var(--ink-blue); line-height: 1.1; white-space: nowrap; }
  .holder-role { font-size: 18px; color: var(--ink-grey); margin-top: 2px; }

  .contact { position: absolute; left: 43px; top: 130px; color: var(--ink-grey); font-size: 18px; }
  .contact-row { display: flex; align-items: center; gap: 6px; height: 28px; white-space: nowrap; }
  .contact-row .phone { color: var(--ink-blue); font-weight: 600; font-size: 21px; }
  .contact-row .cell { font-size: 14px; margin-left: 8px; }
  .contact-row .cell b { font-size: 19px; font-weight: 600; color: var(--ink-blue); }
  .address { position: absolute; left: 43px; top: 222px; font-size: 17px; color: var(--ink-grey); line-height: 22px; }
  .address-lines { padding-left: 24px; white-space: nowrap; }
  .address svg { position: absolute; left: 0; top: 2px; }

  .back-brand {
    position: absolute; left: 340px; top: 244px;
    font-weight: 800; font-size: 64px; line-height: 1; color: var(--watermark);
    letter-spacing: -1px; white-space: nowrap;
  }
  .website {
    position: absolute; left: 0; right: 0; top: 360px;
    text-align: center; font-size: 19px; font-weight: 600; line-height: 24px;
    letter-spacing: 5px; color: var(--navy-deep); white-space: nowrap;
  }
</style>
</head>
<body>
<main class="stage">
  <section class="card card-front">
    <div class="brand-name">B.H.L. Cargo</div>
  </section>

  <section class="card card-back">
    <svg class="back-art" width="744" height="401" viewBox="0 0 744 401" aria-hidden="true">
      <defs>
        <linearGradient id="navyFade" x1="0" y1="0" x2="1" y2="1">
          <stop offset="0" stop-color="#1d5c98"/>
          <stop offset="1" stop-color="#0c2f58"/>
        </linearGradient>
      </defs>
      <path d="M0 326 L310 326 C370 326 385 108 470 108 L744 108 L744 401 L0 401 Z" fill="url(#navyFade)"/>
      <path d="M0 338 L744 338 L744 344 L0 344 Z" fill="#3a8fd0"/>
      <path d="M0 348 L744 348 L744 401 L0 401 Z" fill="#2fa9e2"/>
      <path d="M0 356 L744 356 L744 401 L0 401 Z" fill="#5cc3ee"/>
    </svg>

    <div class="holder">
      <div class="holder-name">Nome Sobrenome</div>
      <div class="holder-role">cargo na empresa</div>
    </div>

    <div class="contact">
      <div class="contact-row">
        <svg width="20" height="20" viewBox="0 0 20 20" aria-hidden="true"><circle cx="10" cy="10" r="9" fill="none" stroke="#1b4f8c" stroke-width="1.6"/><path d="M7 5.5 L9 8 L8 9.5 C8.6 11 9.3 11.7 10.5 12.3 L12 11 L14.5 13 L13.5 14.5 C10 14.5 5.5 10 5.5 6.5 Z" fill="#1b4f8c"/></svg>
        <span class="phone">(44) 3555-0182</span>
        <span class="cell">cel. <b>(44) 9555-0147</b></span>
      </div>
      <div class="contact-row">
        <svg width="20" height="14" viewBox="0 0 20 14" aria-hidden="true"><rect x="1" y="1" width="18" height="12" fill="none" stroke="#1b4f8c" stroke-width="1.6"/><path d="M1 1 L10 8 L19 1" fill="none" stroke="#1b4f8c" stroke-width="1.6"/></svg>
        <span>contato@bhlcargo.com.br</span>
      </div>
    </div>

    <div class="address">
      <svg width="16" height="22" viewBox="0 0 16 22" aria-hidden="true"><path d="M8 1 C4 1 1 4 1 8 C1 13 8 21 8 21 C8 21 15 13 15 8 C15 4 12 1 8 1 Z" fill="#1b4f8c"/><circle cx="8" cy="8" r="2.6" fill="#fff"/></svg>
      <div class="address-lines">
        R. Nome da rua, 1234<br>Jd. Nome do Bairro<br>CEP 87654-321<br>Cidade - Estado
      </div>
    </div>

    <div class="back-brand">B.H.L. Cargo</div>
    <div class="website">www.bhlcargo.com.br</div>
  </section>
</main>
</body>
</html>
```